Email Template for AI Website Builder Marketing Campaign

Update: All the designs submitted have too much content for an email template. I have attached a mockup example of a simplified design. Please follow this guideline to revise your design to be less "wordy" and have less content to optimize the delivery rate of the emails. I have also attached the images I used to create the mockup. Feel free to use these images for your revised designs.
Original Brief:
I need a catchy email template for my new AI Website Builder, WebQuilt.ai. The template must be professional, colorful, yet not too complex. The concept of the product is this:
WebQuilt uses Artificial Intelligence (AI) to instantly build stunning websites, absolutely FREE. The user simply specifies their business name and business category (industry), and their stunning new website appears before their eyes!
The template will be used in MailChimp, so please provide the code that I can simply paste into the email body.
Here is a screenshot of our new website (which is not online yet) so you can match the color scheme and style of the email template to the new website design:
https://pixbinstore.com/art_img/7310582/2208634/48165027/9qrt41hwk826zlmpb3nqd7wyex_image.jpg
Let me know if you have any questions.
Thanks!
All submitted designs are too lengthy (too much content) for an email template. I will provide a mockup showing a sample of how you can simplify your design to function better as an email template and better suit my needs. I appreciate your patience!

```html
<!DOCTYPE html>
<html lang="en">
<head>
<meta charset="utf-8">
<title>WebQuilt – Build Your Website with AI</title>
<link href="https://fonts.googleapis.com/css2?family=Raleway:wght@300;400;500;700&family=Nunito:wght@300;400;600;700&display=swap" rel="stylesheet">
<style>
:root{
  --blue-bright:#1a8cf0;
  --ink:#1e2430;
  --text:#4a4f5a;
  --muted:#8a909a;
  --light-bg:#f1f5f8;
  --card-border:#8fb6d8;
  --footer:#2a2a2d;
  --footer-dark:#1d1d1f;
}
*{margin:0;padding:0;box-sizing:border-box}
html,body{width:1200px;height:5223px;overflow:hidden;background:#fff}
body{font-family:"Nunito",sans-serif;color:var(--text)}
.canvas{position:relative;width:1200px;height:5223px;overflow:hidden}
.abs{position:absolute}
h1,h2,h3{font-family:"Raleway",sans-serif;font-weight:400;color:var(--ink)}
h1 strong,h2 strong{font-weight:700}
.eyebrow{font-size:21px;color:var(--blue-bright);font-weight:400;line-height:28px}
.copy{font-size:20px;line-height:37.5px;color:var(--text);font-weight:300}

/* header */
.brand{display:flex;align-items:center;gap:14px;font-size:26px;color:var(--ink);font-weight:600}
.brand-mark{width:40px;height:40px;border-radius:50%;background:var(--blue-bright)}
.top-nav{top:24px;left:503px;font-size:18px;color:var(--ink)}
.top-nav span{position:absolute;white-space:nowrap}

/* hero */
.hero-photo{left:0;top:118px;width:624px;height:584px;background:radial-gradient(circle at 62% 48%,#3aa0ff 0,#2a4f9a 28%,#5c3a7a 55%,#c4744e 85%,#e29a62 100%)}
.hero-accent-bottom{left:0;top:660px;width:243px;height:114px;background:var(--blue-bright);border-radius:0 0 40px 0}
.hero-accent-top{left:497px;top:77px;width:200px;height:120px;background:var(--blue-bright);border-radius:60px 0 0 0}
.hero-panel{left:624px;top:77px;width:576px;height:760px;border-radius:120px 0 0 120px;background:radial-gradient(circle at 90% 20%,#15447e 0,#0c2a55 45%,#081b3c 100%)}
.hero-copy{left:669px;top:232px;width:440px;color:#fff}
.hero-copy .eyebrow{color:#2e9bff}
.hero-copy h1{color:#fff;font-size:44px;line-height:55px;margin-top:12px}
.hero-copy p{font-size:22px;line-height:42px;color:#e6eef8;margin-top:34px;padding-left:6px}
.hero-btn{left:675px;top:586px;width:312px;height:77px;line-height:77px;text-align:center;background:var(--blue-bright);color:#fff;font-weight:600;font-size:21px;border-radius:40px;text-transform:uppercase}

/* generator */
.robots{left:111px;top:811px;width:436px;height:393px;background:linear-gradient(180deg,#f4f6f8 0,#cfd7dd 60%,#9fb0bd 100%);border-radius:6px}
.gen-copy{left:630px;top:900px;width:450px}
.gen-copy h2{font-size:37px;margin-top:10px}
.gen-copy .copy{margin-top:20px}

/* how */
.how{left:0;top:1204px;width:1200px;height:692px;background:linear-gradient(180deg,#1a86e6,#0f7bdb)}
.how-head{top:1268px;left:0;width:1200px;text-align:center;color:#fff}
.how-head .small{font-size:21px}
.how-head h2{color:#fff;font-size:38px;margin-top:6px}
.how-head p{font-size:20.5px;line-height:38px;margin-top:14px;font-weight:300}
.pill{top:1484px;width:233px;height:345px;background:#fff;border-radius:116px;text-align:center}
.pill .icon{position:absolute;left:53px;width:126px;height:126px;border-radius:50%;background:radial-gradient(circle at 40% 35%,#38b4ff,#0a78d8)}
.pill .icon svg{position:absolute;left:33px;top:33px;width:60px;height:60px}
.pill h3{position:absolute;left:0;width:100%;font-family:"Nunito",sans-serif;font-size:25px;font-weight:400}
.pill p{position:absolute;left:18px;width:197px;font-size:19.5px;line-height:30px;color:var(--muted);font-weight:300}

/* features */
.dotted-v{border-left:2px dotted #888}
.dotted-h{border-top:2px dotted #888}
.diamond-photo{width:285px;height:285px;transform:rotate(45deg);border-radius:32px}
.diamond-outline{width:144px;height:144px;transform:rotate(45deg);border:2px solid #2a9cf2;border-radius:18px}
.diamond-solid{width:68px;height:68px;transform:rotate(45deg);border-radius:12px;background:linear-gradient(135deg,#38b4ff,#0a7ad8)}
.feature-copy{width:390px}
.feature-copy h2{font-size:37px;line-height:49px;margin-top:10px;font-weight:500}
.feature-copy .copy{margin-top:22px}

/* benefits */
.benefits{left:0;top:2980px;width:1200px;height:817px;background:var(--light-bg)}
.tile{width:316px;height:316px;border:2px solid var(--card-border);border-radius:8px;background:var(--light-bg)}
.tile svg{position:absolute;left:28px;top:28px;width:76px;height:76px}
.tile h3{position:absolute;left:28px;top:128px;font-family:"Nunito",sans-serif;font-size:25px;font-weight:400}
.tile p{position:absolute;left:28px;top:180px;width:262px;font-size:20.5px;line-height:37.5px;font-weight:300;color:var(--text)}

/* journey */
.journey{left:0;top:3797px;width:1200px;height:552px;background:linear-gradient(100deg,#3a1c9e 0,#2c2bb0 45%,#1e44bd 80%,#2347c4 100%)}
.journey-art{left:610px;top:3830px;width:560px;height:519px;background:radial-gradient(circle at 30% 38%,rgba(120,160,255,.55) 0,rgba(70,90,230,.3) 25%,rgba(40,50,180,0) 55%),radial-gradient(circle at 78% 55%,rgba(90,140,255,.35) 0,rgba(40,60,190,0) 45%)}
.journey-copy{left:111px;top:3880px;width:430px;color:#fff}
.journey-copy .eyebrow{color:#4aa8ff}
.journey-copy h2{color:#fff;font-size:38px;margin-top:6px}
.journey-copy p{font-size:20.5px;line-height:37.5px;margin-top:22px;font-weight:300;color:#eef}
.get-started{display:flex;align-items:center;gap:18px;margin-top:42px;font-weight:700;font-size:21px}
.get-started i{display:block;width:38px;height:38px;background:#3da4ff;border-radius:6px}

/* testimonials */
.testi-copy{left:111px;top:4515px;width:340px}
.testi-copy h2{font-size:38px;margin-top:10px;font-weight:500}
.testi-copy .copy{margin-top:20px}
.quote-card{top:4436px;width:294px;height:345px;color:#fff}
.quote-card .stars{position:absolute;top:18px;width:100%;text-align:center;color:#ffc21a;font-size:17px;letter-spacing:10px}
.quote-card .frame{position:absolute;left:14px;top:54px;width:266px;height:193px;border:1.5px solid rgba(255,255,255,.55)}
.quote-card .frame p{position:absolute;left:16px;top:28px;width:234px;text-align:center;font-size:16.5px;line-height:33px}
.quote-card .frame b{position:absolute;right:12px;bottom:-6px;font-family:Georgia,serif;font-size:40px;color:#4ab2ff;line-height:1}
.quote-card .name{position:absolute;top:257px;width:100%;text-align:center;font-size:17px}
.quote-card .role{position:absolute;top:280px;width:100%;text-align:center;font-size:11px;color:#d6e6f6}
.avatar{position:absolute;left:117px;top:315px;width:60px;height:60px;border-radius:50%;border:3px solid #fff}

/* footer */
.footer{left:0;top:4866px;width:1200px;height:298px;background:var(--footer)}
.footer-brand{left:0;top:4920px;width:1200px;display:flex;justify-content:center;align-items:center;gap:16px;color:#fff;font-size:34px}
.footer-brand i{width:58px;height:58px;border-radius:50%;background:var(--blue-bright);display:block}
.footer-nav{top:5020px;left:0;width:1200px;display:flex;justify-content:center;gap:44px;color:#fff;font-size:16.5px}
.socials{top:5079px;left:0;width:1200px;display:flex;justify-content:center;gap:14px}
.socials span{width:32px;height:32px;border-radius:50%;background:#fff;display:block}
.legal{left:0;top:5164px;width:1200px;height:59px;background:var(--footer-dark);color:#cfcfd2;font-size:13.5px;text-align:center;line-height:59px}
</style>
</head>
<body>
<div class="canvas">

  <div class="abs brand" style="left:111px;top:47px"><span class="brand-mark"></span>WebQuilt</div>
  <nav class="abs top-nav">
    <span style="left:0">About WebQuilt</span>
    <span style="left:168px">About AI</span>
    <span style="left:290px">History of AI</span>
    <span style="left:440px">Make Money Guide</span>
  </nav>

  <div class="abs hero-accent-top"></div>
  <div class="abs hero-accent-bottom"></div>
  <div class="abs hero-photo" role="img" aria-label="Glowing robotic head in profile with circuit lines"></div>
  <div class="abs hero-panel" role="img" aria-label="Dark navy panel with faint circuit traces"></div>
  <div class="abs hero-copy">
    <div class="eyebrow">Let Artificial Intelligence</div>
    <h1>Build Your Stunning<br>Website <strong>Instanly</strong></h1>
    <p>Enter your business name and industry. Your new site appears in seconds.</p>
  </div>
  <a class="abs hero-btn">Build my free website</a>

  <div class="abs robots" role="img" aria-label="Two white humanoid robots standing in thought"></div>
  <div class="abs gen-copy">
    <div class="eyebrow">AI Website Generator</div>
    <h2>Build a Website <strong>with AI</strong></h2>
    <p class="copy">No code, no designer, no cost. Just two details and WebQuilt does the rest.</p>
  </div>

  <section class="abs how"></section>
  <div class="abs how-head">
    <div class="small">How you</div>
    <h2>Create Website <strong>with AI</strong></h2>
    <p>Tell us your business name and category, and AI builds a professional site for you.</p>
  </div>

  <div class="abs pill" style="left:111px">
    <div class="icon" style="top:46px"><svg viewBox="0 0 60 60" fill="none" stroke="#fff" stroke-width="2.5"><rect x="17" y="6" width="26" height="48" rx="4"/><circle cx="30" cy="28" r="8"/><line x1="26" y1="48" x2="34" y2="48"/></svg></div>
    <h3 style="top:195px">Mobile Focused</h3>
    <p style="top:240px">Looks great on every screen</p>
  </div>
  <div class="abs pill" style="left:360px">
    <h3 style="top:62px">Flexible Use</h3>
    <p style="top:106px">Fits any business or idea</p>
    <div class="icon" style="top:191px"><svg viewBox="0 0 60 60" fill="none" stroke="#fff" stroke-width="2.5"><circle cx="30" cy="30" r="14"/><path d="M30 6v8M30 46v8M6 30h8M46 30h8"/></svg></div>
  </div>
  <div class="abs pill" style="left:608px">
    <div class="icon" style="top:46px"><svg viewBox="0 0 60 60" fill="none" stroke="#fff" stroke-width="2.5"><path d="M14 8h32v28H14z"/><rect x="6" y="38" width="48" height="14" rx="4" fill="#fff"/><text x="30" y="49" text-anchor="middle" font-family="Nunito,sans-serif" font-weight="700" font-size="11" fill="#0a78d8" stroke="none">FREE</text></svg></div>
    <h3 style="top:195px">Free to Try</h3>
    <p style="top:240px">Start today at no cost</p>
  </div>
  <div class="abs pill" style="left:857px">
    <h3 style="top:62px">Cloud Strength</h3>
    <p style="top:106px">Fast, secure hosting</p>
    <div class="icon" style="top:191px"><svg viewBox="0 0 60 60" fill="none" stroke="#fff" stroke-width="2.5"><path d="M18 30a8 8 0 0 1 2-15 11 11 0 0 1 21 2 7 7 0 0 1 1 13z"/><path d="M8 36l10 10h8v8M52 36L42 46h-8v8"/></svg></div>
  </div>

  <div class="abs dotted-v" style="left:45px;top:2003px;height:450px"></div>
  <div class="abs dotted-h" style="left:45px;top:2453px;width:1111px"></div>
  <div class="abs dotted-v" style="left:1155px;top:2453px;height:446px"></div>

  <div class="abs diamond-outline" style="left:143px;top:2128px"></div>
  <div class="abs diamond-photo" style="left:255px;top:2057px;background:radial-gradient(circle,#6fd0ff 0,#1f5a9a 25%,#0f2746 60%,#0a1a30 100%)" role="img" aria-label="Hand holding a glowing digital globe"></div>
  <div class="abs diamond-solid" style="left:564px;top:2081px"></div>
  <div class="abs feature-copy" style="left:705px;top:2020px">
    <div class="eyebrow">Advancements in AI</div>
    <h2>Technology and Their Influence on Wbsite Building</h2>
    <p class="copy">AI now writes, designs and lays out pages in moments.</p>
  </div>

  <div class="abs feature-copy" style="left:111px;top:2543px">
    <div class="eyebrow">The Advantages of</div>
    <h2>Using AI for Website Building</h2>
    <p class="copy">Launch faster, spend less, and update whenever you like.</p>
  </div>
  <div class="abs diamond-outline" style="left:917px;top:2629px"></div>
  <div class="abs diamond-photo" style="left:664px;top:2558px;background:radial-gradient(circle at 50% 45%,#d8d4cc 0,#b9ad98 30%,#6d6256 70%,#3d3630 100%)" role="img" aria-label="Humanoid robot in a beige suit seated in an office"></div>
  <div class="abs diamond-solid" style="left:570px;top:2581px"></div>

  <section class="abs benefits"></section>
  <div class="abs tile" style="left:111px;top:3063px">
    <svg viewBox="0 0 76 76" fill="none" stroke="#1a8cf0" stroke-width="2.5"><circle cx="44" cy="40" r="20"/><path d="M44 40l8-8M40 14h8M44 14v6M8 34h14M4 42h14M10 50h14"/></svg>
    <h3>Speed and Efficiency</h3><p>Your site is ready in seconds.</p>
  </div>
  <div class="abs tile" style="left:442px;top:3063px">
    <svg viewBox="0 0 76 76" fill="none" stroke="#1a8cf0" stroke-width="2.5"><path d="M30 18C14 26 12 52 20 62h36c8-10 6-36-10-44z"/><circle cx="38" cy="42" r="11"/><path d="M28 10l5 6h10l5-6"/></svg>
    <h3>Cost Effective</h3><p>Free to build, no agency fees.</p>
  </div>
  <div class="abs tile" style="left:773px;top:3063px">
    <svg viewBox="0 0 76 76" fill="none" stroke="#1a8cf0" stroke-width="2.5"><circle cx="38" cy="34" r="26"/><circle cx="38" cy="28" r="8"/><path d="M22 50c4-8 10-10 16-10s12 2 16 10"/></svg>
    <h3>User Friendly</h3><p>No coding skills needed.</p>
  </div>
  <div class="abs tile" style="left:111px;top:3394px">
    <svg viewBox="0 0 76 76" fill="none" stroke="#1a8cf0" stroke-width="2.5"><circle cx="38" cy="38" r="20"/><path d="M38 8v8M38 60v8M8 38h8M60 38h8M32 44V32M38 46V30M44 44V34"/></svg>
    <h3>Customization</h3><p>Tweak colors, text and layout.</p>
  </div>
  <div class="abs tile" style="left:442px;top:3394px">
    <svg viewBox="0 0 76 76" fill="none" stroke="#1a8cf0" stroke-width="2.5"><circle cx="44" cy="30" r="20"/><path d="M44 18v12l8 6"/><path d="M12 30c0 20 14 36 34 38l4-8-8-6-5 4c-7-4-12-10-14-18l5-4-4-9z"/></svg>
    <h3>24/7 Availability</h3><p>Build any time, day or night.</p>
  </div>
  <div class="abs tile" style="left:773px;top:3394px">
    <svg viewBox="0 0 76 76" fill="none" stroke="#1a8cf0" stroke-width="2.5"><path d="M38 8l12 7v14l-12 7-12-7V15zM24 36l12 7v14l-12 7-12-7V43zM52 36l12 7v14l-12 7-12-7V43z"/></svg>
    <h3>Scalability</h3><p>Grows as your business grows.</p>
  </div>

  <section class="abs journey"></section>
  <div class="abs journey-art" role="img" aria-label="Glowing wireframe robot head beside a luminous sphere"></div>
  <div class="abs journey-copy">
    <div class="eyebrow">Begin Your</div>
    <h2>Journey <strong>with AI Design</strong></h2>
    <p>Your stunning website is one click away. Try it free today.</p>
    <div class="get-started"><i></i>GET STARTED</div>
  </div>

  <div class="abs testi-copy">
    <div class="eyebrow">Testimonials</div>
    <h2>Our Client Say’s</h2>
    <p class="copy">What early users say.</p>
  </div>
  <div class="abs quote-card" style="left:478px;background:#1f5fae">
    <div class="stars">★★★★★</div>
    <div class="frame"><p>“My site was live in under a minute. Simple and beautiful.”</p><b>”</b></div>
    <div class="name">Mara Lindqvist</div>
    <div class="role">Happy Residential Customer</div>
    <div class="avatar" style="background:#b07a5c" role="img" aria-label="Customer portrait"></div>
  </div>
  <div class="abs quote-card" style="left:793px;background:#1c82bd">
    <div class="stars">★★★★★</div>
    <div class="frame"><p>“Two details and I had a professional website. Amazing.”</p><b>”</b></div>
    <div class="name">Tobin Ashcroft</div>
    <div class="role">Happy Residential Customer</div>
    <div class="avatar" style="background:#6b5a4e" role="img" aria-label="Customer portrait"></div>
  </div>

  <footer class="abs footer"></footer>
  <div class="abs footer-brand"><i></i>WebQuilt</div>
  <nav class="abs footer-nav"><span>ABOUT WEBQUILT</span><span>ABOUT AI</span><span>HISTORY OF AI</span><span>MAKE MONEY GUIDE</span></nav>
  <div class="abs socials" aria-label="Social links"><span></span><span></span><span></span><span></span><span></span><span></span></div>
  <div class="abs legal">COPYRIGHT © 2023 | PRIVACY POLICY</div>

</div>
</body>
</html>
```